Business Card Design

Business Card for professional consulting firm working with large financial institutions.

Target Market(s)

Executive buyers

Industry/Entity Type

Banking

Contact Information for Business Card

Mild creativity wanted. Not boring, but do elaborate artwork.

Font styles to use
Serif
Sans Serif

Colors

Designer to choose colors to be used in the design.

Requirements
Must have
• Standard business card features - company name, individual name, telephone, website, email, locations.
Nice to have
• Two colors
Should not have
• too many colors, fancy printing, cartoons.

```html
<!DOCTYPE html>
<html lang="en">
<head>
<meta charset="utf-8">
<title>Northvale Advisory – Business Card</title>
<link rel="stylesheet" href="https://fonts.googleapis.com/css2?family=Montserrat:wght@400;500;800&family=Noto+Serif:wght@400&display=swap">
<style>
  :root {
    --backdrop: #cdd1d1;
    --card-white: #f7f7f6;
    --card-black: #1d1d1b;
    --ink: #1a1a1a;
    --ink-soft: #4a4a4a;
    --rule: #b9b9b9;
    --mark-grey: #9a9a9a;
    --paper-white: #ffffff;
  }
  * { margin: 0; padding: 0; box-sizing: border-box; }
  html, body {
    width: 1200px; height: 1050px; overflow: hidden;
    background: var(--backdrop);
  }
  .canvas {
    position: relative; width: 1200px; height: 1050px;
    display: flex; flex-direction: column; align-items: center;
    justify-content: center; gap: 90px;
  }
  .card {
    position: relative; width: 700px; height: 400px;
    box-shadow: 0 6px 18px rgba(0,0,0,0.12);
  }
  .card--front { background: var(--card-white); color: var(--ink); }
  .card--back {
    background: var(--card-black);
    display: flex; align-items: center; justify-content: center;
  }

  .brand {
    display: flex; align-items: center; gap: 14px;
    font-family: "Noto Serif", Georgia, serif; font-weight: 400;
  }
  .brand__dot { border-radius: 50%; flex: none; }
  .card--front .brand {
    position: absolute; left: 70px; top: 58px;
    font-size: 38px; color: var(--ink);
  }
  .card--front .brand__dot { width: 14px; height: 14px; background: var(--mark-grey); }
  .card--back .brand { font-size: 50px; color: var(--paper-white); }
  .card--back .brand__dot { width: 18px; height: 18px; background: var(--paper-white); }

  .rule {
    position: absolute; left: 70px; right: 60px; height: 1px;
    background: var(--rule);
  }
  .rule--top { top: 150px; }
  .rule--bottom { top: 282px; left: 330px; }

  .contact {
    position: absolute; left: 70px; top: 178px;
    list-style: none;
    font-family: "Montserrat", Arial, sans-serif; font-size: 15px;
    color: var(--ink-soft); line-height: 24px;
  }
  .contact li { display: flex; align-items: center; gap: 12px; }
  .contact svg { width: 14px; height: 14px; flex: none; }

  .person {
    position: absolute; right: 60px; top: 212px; text-align: right;
    font-family: "Montserrat", Arial, sans-serif;
  }
  .person__name { font-size: 25px; font-weight: 800; color: var(--ink); letter-spacing: 0.2px; }
  .person__title { font-size: 14px; font-weight: 500; color: var(--ink-soft); margin-top: 2px; }

  .address {
    position: absolute; right: 60px; top: 300px; text-align: right;
    font-family: "Montserrat", Arial, sans-serif; font-size: 16px;
    color: var(--ink-soft); line-height: 24px; font-style: normal;
  }
</style>
</head>
<body>
<main class="canvas">
  <section class="card card--front" aria-label="Business card front">
    <div class="brand"><span class="brand__dot"></span>Northvale Advisory</div>
    <div class="rule rule--top"></div>
    <ul class="contact">
      <li>
        <svg viewBox="0 0 16 16" aria-hidden="true"><path d="M4 1.5l2.2 3-1.3 1.6c.8 1.8 2.2 3.2 4 4l1.6-1.3 3 2.2-1.1 2.6C7 13.4 2.6 9 2 2.6z" fill="var(--ink-soft)"/></svg>
        000.000.0000
      </li>
      <li>
        <svg viewBox="0 0 16 16" aria-hidden="true"><rect x="1.5" y="3.5" width="13" height="9" fill="none" stroke="var(--ink-soft)" stroke-width="1.2"/><path d="M1.5 3.5L8 9l6.5-5.5" fill="none" stroke="var(--ink-soft)" stroke-width="1.2"/></svg>
        daniel@northvaleadvisory.com
      </li>
      <li>
        <svg viewBox="0 0 16 16" aria-hidden="true"><g fill="none" stroke="var(--ink-soft)" stroke-width="1.1"><circle cx="8" cy="8" r="6.5"/><ellipse cx="8" cy="8" rx="2.8" ry="6.5"/><path d="M1.5 8h13M2.6 4.6h10.8M2.6 11.4h10.8"/></g></svg>
        www.northvaleadvisory.com
      </li>
    </ul>
    <div class="person">
      <div class="person__name">Daniel HARPER</div>
      <div class="person__title">Managing Director</div>
    </div>
    <div class="rule rule--bottom"></div>
    <address class="address">418 N Market Street 2210<br>Cedar Falls, MS 39110</address>
  </section>

  <section class="card card--back" aria-label="Business card back">
    <div class="brand"><span class="brand__dot"></span>Northvale Advisory</div>
  </section>
</main>
</body>
</html>
```